Velmorytrips.com web design project + logo design

Hi,

We are a Russian online tour operator - roamquiltex.com

We are looking to tranmsfer our domain to velmorytrips.com. The website and logo need to be velmoryesque - we are not looking to change our functionality, but we need to make the website much more attracitve to clients, much more wild looking but at the same time remaining a professional travel company.

The main concept of the website should be innovative travel (as velmory was an innovator). Alternatively, you could go down the artist route and go down the draw / design your own tour road.

On our website the customer is able to combine travel services (hotels, flights, Visa services, and soon chauffeur, car rental etc...) put it into their basket (the basket definitely has to look better than it is at the moment) and pay for it in one go by card.

We are also stressin our customer support with web chat, call centre etc... (call centre number at the top of the page)

We aim to provide an easy user experience, but we need to make it have some more style, so I will be waiting for what you guys can come up with.
Let me know if you have any questions - skype is: mrkostelin

Industry/Entity Type

It Company

Logo Text

Requirements
Must have
• It is quite a simple task - to take the existing website roamquiltex.com and velmorysize it to create velmorytrips.com, the functionality of the website will remain the same and there are not many pages in the website. Homepage, Checkout step1, Checkout step 2 (you can view both of these if you select a service) and the generic pages for T&C''s, Privacy policy etc...

IMPORTANT UPDATE

We are also looking at how the search results will look in the designs, (please do a search on our website for hotel / flight)

```html
<!DOCTYPE html>
<html lang="ru">
<head>
<meta charset="utf-8">
<title>Velmorytrips.com — оформление заказа</title>
<link href="https://fonts.googleapis.com/css2?family=Open+Sans:wght@300;400;600&family=PT+Serif:wght@400;700&family=Arimo&family=Tinos&display=swap" rel="stylesheet">
<style>
:root{
  --paper:#f2efe3;
  --brand:#6c1c00;
  --route:#6b1200;
  --ink:#231006;
  --field:#e3dec2;
  --white:#ffffff;
  --grey:#ececec;
}
html,body{margin:0;padding:0;width:1200px;height:844px;overflow:hidden;background:var(--paper);}
.stage{position:absolute;left:0;top:0;width:1280px;height:900px;transform:scale(.9375);transform-origin:0 0;
  background:radial-gradient(ellipse at 30% 40%,#f5f2e7 0%,#efebdd 70%,#ebe6d6 100%);color:var(--ink);}
.abs{position:absolute;}
.flight{font-family:"Arimo",Arial,sans-serif;font-size:12px;color:var(--route);line-height:20px;}
.flight .carrier{font-family:"Arimo",Arial,sans-serif;font-size:17px;color:var(--route);margin:8px 0 14px;height:28px;line-height:28px;}
.flight dl{margin:0;display:grid;grid-template-columns:99px auto;}
.flight dt,.flight dd{margin:0;line-height:20.5px}
.terms{font-family:"Open Sans",sans-serif;font-size:13px;color:#1b0a04;letter-spacing:.2px}
.terms span{font-size:14px}
.price-tag,.total{background:var(--brand);color:#fff;font-family:"PT Serif",serif;font-weight:700;display:flex;align-items:center;justify-content:center;}
.price-tag{left:949px;top:194px;width:146px;height:39px;font-size:19px;}
.total{left:485px;top:453px;width:311px;height:39px;font-size:18px;}
.label{font-family:"Open Sans",sans-serif;font-weight:600;font-size:14px;color:#231006;}
.field{height:40px;background:var(--field);font-family:"Tinos","Times New Roman",serif;font-size:19px;color:#1b0a04;display:flex;align-items:center;padding-left:14px;box-sizing:border-box;}
.field.center{justify-content:center;padding:0}
.input{height:40px;background:var(--white);box-sizing:border-box;}
.prefix{left:198px;top:668px;width:51px;height:31px;background:var(--grey);font-family:"Tinos",serif;font-size:16px;display:flex;align-items:center;justify-content:center;}
.select{left:456px;top:664px;width:120px;height:40px;background:var(--white);}
.select .sep{position:absolute;left:89px;top:6px;bottom:6px;border-left:1px dashed #cfcfcf}
.select svg{position:absolute;left:100px;top:16px}
.check{width:16px;height:16px;}
.agree{font-family:"Open Sans",sans-serif;font-weight:600;font-size:14px;color:#1b0a04;}
.pay-title{left:752px;top:582px;font-family:"PT Serif",serif;font-size:19px;color:#1b0a04;letter-spacing:.3px}
.pay-note{left:755px;top:621px;width:300px;font-family:"Open Sans",sans-serif;font-weight:300;font-size:13.6px;line-height:15.2px;color:#1b0a04;margin:0}
</style>
</head>
<body>
<div class="stage">

  <section class="abs flight" style="left:192px;top:7px">
    <div>Рейс: Varnholm (VQH) → Caspian Gate Intl (CQX)</div>
    <div>Продолжительность перелета: 2ч50м</div>
    <div class="carrier">Skyrell</div>
    <dl><dt>Номер рейса:</dt><dd>SK4451</dd><dt>Вылет:</dt><dd>14:40, 22 Июнь 2013</dd><dt>Прилет:</dt><dd>18:30, 22 Июнь 2013</dd></dl>
  </section>

  <section class="abs flight" style="left:640px;top:7px">
    <div>Рейс: Caspian Gate Intl (CQX) → Varnholm (VQH)</div>
    <div>Продолжительность перелета: 3ч00м</div>
    <div class="carrier">Skyrell</div>
    <dl><dt>Номер рейса:</dt><dd>SK4452</dd><dt>Вылет:</dt><dd>10:40, 02 Июль 2013</dd><dt>Прилет:</dt><dd>12:40, 02 Июль 2013</dd></dl>
  </section>

  <div class="abs terms" style="left:196px;top:205px">УСЛОВИЯ ВОЗВРАТА И ОБМЕНА БИЛЕТОВ &nbsp;- &nbsp;<span>подробнее</span></div>
  <div class="abs price-tag">20862 Руб</div>

  <div class="abs label" style="left:195px;top:257px">Имя</div>
  <div class="abs label" style="left:457px;top:257px">Фамилия</div>
  <div class="abs label" style="left:716px;top:257px">Дата рождения</div>
  <div class="abs label" style="left:977px;top:257px">Пол</div>
  <div class="abs field" style="left:193px;top:285px;width:241px">ORLAN</div>
  <div class="abs field" style="left:454px;top:285px;width:241px">MERIKOV</div>
  <div class="abs field" style="left:714px;top:285px;width:241px">02 июнь 1989</div>
  <div class="abs field center" style="left:975px;top:285px;width:121px">мужчина</div>

  <div class="abs label" style="left:195px;top:341px">Номер Документа</div>
  <div class="abs label" style="left:457px;top:341px">Страна выдачи</div>
  <div class="abs label" style="left:716px;top:341px">Годен до</div>
  <div class="abs field" style="left:193px;top:365px;width:241px;padding-left:17px">AZ 47201938564</div>
  <div class="abs field" style="left:454px;top:365px;width:241px">Baku</div>
  <div class="abs field" style="left:714px;top:365px;width:241px"></div>
  <div class="abs label" style="left:982px;top:371px;font-size:13px">Без даты</div>
  <svg class="abs check" style="left:1053px;top:373px" viewBox="0 0 16 16"><rect width="16" height="16" rx="3" fill="#231006"/><path d="M4 8.2l2.6 2.6L12 5.4" stroke="#fff" stroke-width="1.8" fill="none"/></svg>

  <div class="abs total">Итоговая сумма: 20862 Руб</div>

  <div class="abs label" style="left:195px;top:548px">Имя - Латинскими буквами</div>
  <div class="abs label" style="left:457px;top:548px">Фамилия - Латинскими буквами</div>
  <div class="abs input" style="left:193px;top:576px;width:241px"></div>
  <div class="abs input" style="left:454px;top:576px;width:241px"></div>

  <div class="abs label" style="left:195px;top:636px">Мобильный телефон</div>
  <div class="abs label" style="left:459px;top:636px">Пол</div>
  <div class="abs input" style="left:193px;top:663px;width:241px"></div>
  <div class="abs prefix">+7</div>
  <div class="abs select"><span class="sep"></span><svg width="10" height="7" viewBox="0 0 10 7"><path d="M0 0h10L5 7z" fill="#231006"/></svg></div>

  <div class="abs label" style="left:195px;top:723px">Email</div>
  <div class="abs label" style="left:457px;top:723px">Подтвердите email</div>
  <div class="abs input" style="left:193px;top:747px;width:241px"></div>
  <div class="abs input" style="left:454px;top:747px;width:241px"></div>

  <svg class="abs check" style="left:195px;top:821px" viewBox="0 0 16 16"><rect width="16" height="16" rx="3" fill="#231006"/><path d="M4 8.2l2.6 2.6L12 5.4" stroke="#fff" stroke-width="1.8" fill="none"/></svg>
  <div class="abs agree" style="left:229px;top:820px">Я ПРИНИМАЮ УСЛОВИЯ ПОЛЬЗОВАНИЯ САЙТА, ОТМЕНЫ И ВОЗВРАТОВ</div>
  <svg class="abs check" style="left:195px;top:853px" viewBox="0 0 16 16"><rect width="16" height="16" rx="3" fill="#231006"/><path d="M4 8.2l2.6 2.6L12 5.4" stroke="#fff" stroke-width="1.8" fill="none"/></svg>
  <div class="abs agree" style="left:229px;top:852px">Я хотел бы получать рассылку о специальных предложениях</div>

  <div class="abs pay-title">ОПЛАТА БАНКОВСКОЙ КАРТЫ</div>
  <p class="abs pay-note">В целях безопасности данные вашей банковской карты на сервере не сохраняются. Чтобы произвести оплату вас автоматически переводят на конфиденциальную страницу в банк клиент, после нажатия клавиши ПРОДОЛЖИТЬ. Подтверждение заказа мы вышлем на указанный вами адрес электронной почты (Поле “Адрес электронной почты” обязательно для заполнения).</p>

</div>
</body>
</html>
```